New Business Card Design Project

I have a logo I would like to use on the business card. I want something that will stand out and that will be remembered.

Target Market(s)

People who collect gems, minerals and crystals.

Contact Information for Business Card

email - tkstonefalcon@mailbrook.net
phone # 617-203-4958

Font styles to use
Serif
Sans Serif
Decorative

Colors

Designer to choose colors to be used in the design.

Requirements
Must have
• The logo...two to choose from.
Nice to have
• An eye catching and memorable way to draw in people who collect gems minerals and crystals.

```html
<!DOCTYPE html>
<html lang="en">
<head>
<meta charset="utf-8">
<title>Falcon Stoneworks – Business Card</title>
<link href="https://fonts.googleapis.com/css2?family=Open+Sans:wght@300;400;600&display=swap" rel="stylesheet">
<style>
  :root {
    --page-bg: #e9e9e7;
    --card-bg: #ffffff;
    --ink: #1d1d21;
    --brand-blue: #2a46c4;
    --brand-blue-light: #3f5fd8;
    --accent-cyan: #33b6e8;
    --soft-grey: #eeeff1;
  }
  html, body {
    margin: 0;
    padding: 0;
    width: 1200px;
    height: 1023px;
    overflow: hidden;
    background: var(--page-bg);
    font-family: "Open Sans", sans-serif;
  }
  .canvas {
    position: relative;
    width: 1200px;
    height: 1023px;
  }
  .card-front {
    position: absolute;
    left: 150px;
    top: 254px;
    width: 900px;
    height: 514px;
    background: linear-gradient(120deg, var(--card-bg) 45%, var(--soft-grey) 100%);
    box-shadow: 0 10px 30px rgba(0,0,0,0.18);
    overflow: hidden;
  }
  .brand {
    position: absolute;
    left: 70px;
    top: 200px;
    display: flex;
    align-items: center;
    gap: 16px;
  }
  .brand-dot {
    width: 34px;
    height: 34px;
    border-radius: 50%;
    background: var(--ink);
  }
  .brand-name {
    font-size: 36px;
    font-weight: 600;
    color: var(--ink);
    letter-spacing: 0.5px;
  }
  .name-band {
    position: absolute;
    left: 0;
    top: 362px;
    width: 470px;
    height: 58px;
    background: linear-gradient(90deg, var(--brand-blue), var(--brand-blue-light));
    display: flex;
    align-items: center;
    padding-left: 44px;
    box-sizing: border-box;
    gap: 14px;
  }
  .person-name {
    color: #ffffff;
    font-weight: 300;
    font-size: 27px;
  }
  .person-position {
    color: var(--accent-cyan);
    font-weight: 300;
    font-size: 20px;
    letter-spacing: 9px;
  }
  .contact {
    position: absolute;
    left: 520px;
    top: 262px;
    list-style: none;
    margin: 0;
    padding: 0;
    color: var(--ink);
    font-size: 24px;
    font-weight: 400;
  }
  .contact li {
    display: flex;
    align-items: center;
    gap: 12px;
    margin-bottom: 8px;
  }
  .contact svg {
    width: 16px;
    height: 16px;
    fill: var(--ink);
  }
</style>
</head>
<body>
  <div class="canvas">
    <section class="card-front">
      <div class="brand">
        <span class="brand-dot"></span>
        <span class="brand-name">Falcon Stoneworks</span>
      </div>

      <div class="name-band">
        <span class="person-name">Your Name</span>
        <span class="person-position">POSITION</span>
      </div>

      <ul class="contact">
        <li>
          <svg viewBox="0 0 16 16" aria-hidden="true"><path d="M4 1 L6.5 4 L5 6 Q6.5 9.5 10 11 L12 9.5 L15 12 L13 15 Q4 14 1 3 Z"/></svg>
          <span>617-203-4958</span>
        </li>
        <li>
          <svg viewBox="0 0 16 16" aria-hidden="true"><path d="M1 3 H15 V13 H1 Z M2 4 L8 9 L14 4 Z" fill-rule="evenodd"/></svg>
          <span>tkstonefalcon@mailbrook.net</span>
        </li>
      </ul>
    </section>
  </div>
</body>
</html>
```